Visitenkarten-Design für Gesundheits- und Ernährungsberaterin
Zielgruppe
Ich bin Gesundheit und Ernährungsberaterin
Zielgruppe sind chronisch Kranke und Gesundheitsbewusste Personen
Aufgabenstellung
Schlichtes aber direkt erkennbares Design.
Mahl mit Maß , Gesundheit und Ernährungsberatung ( gut lesbar , elegant)
Marlene Obruk-Feistinger ( nicht so groß )
Grau ; Grün Töne und gerne etwas rosa
Infos wie Adresse und E-Mail vielleicht in jeweilige Blöcke am unteren Rand

```html
<!DOCTYPE html>
<html lang="de">
<head>
<meta charset="utf-8">
<title>Visitenkarte – Mahl mit Maß</title>
<link rel="stylesheet" href="https://fonts.googleapis.com/css2?family=Tinos&family=Montserrat:wght@400&display=swap">
<style>
  :root {
    --card-grey: #5c6166;
    --band-green: #8a9a3b;
    --accent-pink: #e2275f;
    --ink-white: #ffffff;
    --page-bg: #fdfdfd;
  }
  * { box-sizing: border-box; margin: 0; padding: 0; }
  html, body {
    width: 1174px; height: 1200px; overflow: hidden;
    background: var(--page-bg);
  }
  .sheet { position: relative; width: 1174px; height: 1200px; }
  .card {
    position: absolute; left: 222px;
    width: 733px; height: 407px;
    background: var(--card-grey);
    border-top: 12px solid var(--band-green);
    border-bottom: 12px solid var(--band-green);
    color: var(--ink-white);
  }
  .card--front { top: 167px; }
  .card--back { top: 628px; }
  .card__name {
    position: absolute; top: 114px; left: 0; width: 100%;
    text-align: center;
    font-family: "Tinos", "Times New Roman", serif;
    font-size: 27px; font-weight: 400; line-height: 36px;
  }
  .card__divider {
    position: absolute; top: 172px; left: 159px;
    width: 413px; height: 6px;
  }
  .contact {
    position: absolute; left: 0; top: 212px; width: 100%;
    list-style: none;
    font-family: "Montserrat", Arial, sans-serif;
    font-size: 15px; letter-spacing: 0.06em;
  }
  .contact__item {
    position: relative; height: 23.5px; line-height: 23.5px;
    text-align: center; padding-left: 30px;
  }
  .contact__item--phone { letter-spacing: 0.32em; }
  .contact__icon {
    position: absolute; left: 228px; top: 5px;
    width: 14px; height: 14px;
  }
  .brand {
    position: absolute; top: 130px; left: 0; width: 100%;
    text-align: center;
  }
  .brand__title {
    font-family: "Tinos", "Times New Roman", serif;
    font-size: 40px; font-weight: 400; line-height: 48px;
  }
  .brand__divider {
    display: block; margin: 14px auto 16px;
    width: 413px; height: 6px;
  }
  .brand__tagline {
    font-family: "Montserrat", Arial, sans-serif;
    font-size: 15px; letter-spacing: 0.12em; line-height: 22px;
  }
</style>
</head>
<body>
<main class="sheet">
  <section class="card card--front">
    <h1 class="card__name">Marlene Obruk-Feistinger</h1>
    <svg class="card__divider" viewBox="0 0 413 6" aria-hidden="true">
      <path d="M0 3 Q206 -1 413 3 Q206 7 0 3 Z" fill="var(--accent-pink)"/>
    </svg>
    <ul class="contact">
      <li class="contact__item">
        <svg class="contact__icon" viewBox="0 0 14 14"><path d="M7 1a4.5 4.5 0 0 0-4.5 4.5C2.5 9 7 13 7 13s4.5-4 4.5-7.5A4.5 4.5 0 0 0 7 1z" fill="#fff"/><circle cx="7" cy="5.5" r="1.6" fill="var(--card-grey)"/></svg>
        Lindenstieg 7, 24599 Bordrup
      </li>
      <li class="contact__item contact__item--phone">
        <svg class="contact__icon" viewBox="0 0 14 14"><rect x="4" y="2" width="6" height="10" rx="1" fill="#fff"/><rect x="5" y="3.5" width="4" height="5" fill="var(--card-grey)"/></svg>
        0151/52073815
      </li>
      <li class="contact__item contact__item--phone">
        <svg class="contact__icon" viewBox="0 0 14 14"><path d="M3 2l2.2 0.3 0.8 2.6-1.3 1a7 7 0 0 0 3.4 3.4l1-1.3 2.6 0.8 0.3 2.2c-4.5 1-10-4.5-9-9z" fill="#fff"/></svg>
        04392/8264017
      </li>
      <li class="contact__item">
        <svg class="contact__icon" viewBox="0 0 14 14"><rect x="1.5" y="3" width="11" height="8" fill="#fff"/><path d="M1.5 3l5.5 4.5 5.5-4.5" fill="none" stroke="var(--card-grey)" stroke-width="1"/></svg>
        ernaehrung-mof@postfach.de
      </li>
    </ul>
  </section>

  <section class="card card--back">
    <div class="brand">
      <h2 class="brand__title">Mahl mit Maß</h2>
      <svg class="brand__divider" viewBox="0 0 413 6" aria-hidden="true">
        <path d="M0 3 Q206 -1 413 3 Q206 7 0 3 Z" fill="var(--accent-pink)"/>
      </svg>
      <p class="brand__tagline">Gesundheit und Ernährungsberatung</p>
    </div>
  </section>
</main>
</body>
</html>
```